Bioidentical Hormone Replacement Therapy

I need a rectangular brochure- sized flyer (one page) designed to hand out to patients that will capture their attention. The flyer will display our company name, logo, contact information, website and social media information provided below. We need people to know that we offer a personalized approach to medicine. The main purpose of the flyer is to convey the fact that we offer bioidentical hormone replacement therapy (BHRT) for women and men by a pellet insertion procedure even for non members. Symptoms this can help with are for Women:
Fatigue*
Trouble sleeping*
Irritability*
Anxiousness*
Mood swings*
Low mood*
Night sweats*
Hot flashes or flushes*
Weight gain*
Decreased sex drive*
Discomfort during intercourse*
Low bone density*
and for Men:
Low sex drive*
Increased body fat
(especially in the waist area)*
Loss of muscle mass and strength*
Reduced mental focus*
Feelings of anxiety*
Irritability*
Fatigue*
Elevated blood sugar*
High cholesterol*
Practice name: Brookhaven Internal Medicine
Address: 4382 Larkspur Lane, Columbia, SC. 20917
Phone: 803-671-5394
Email: jtrevor@brookhavenimd.example
Website: https://brookhavenimd.example
Facebook: https://www.facebook.com/profile.php?id=70938265147723
Updates
For sizing 3.5 inch or so by 8.5 inch or so inch is fine. Not sure what is standard printing paper size for flyer.
Target Market(s)
Medical Patients
Industry/Entity Type
Healthcare
Look and feel

```html
<!DOCTYPE html>
<html lang="en">
<head>
<meta charset="utf-8">
<title>Natural Hormone for Women and Men – Brookhaven Internal Medicine</title>
<link rel="stylesheet" href="https://fonts.googleapis.com/css2?family=Bebas+Neue&family=Montserrat:wght@300;400;600;700&display=swap">
<style>
:root{
  --stage:#b4b4b6;
  --paper:#ffffff;
  --ink:#25262f;
  --navy:#2c2e3c;
  --blue:#3a62b4;
  --blue-light:#5479c7;
  --tick:#4a73c6;
  --photo-a:#e9e3da;
  --photo-b:#b9c6da;
  --doc-a:#8a2430;
  --doc-b:#d8b39a;
}
*{margin:0;padding:0;box-sizing:border-box}
html,body{width:1200px;height:2356px;overflow:hidden}
body{background:var(--stage);position:relative;font-family:"Montserrat",sans-serif}
.flyer{
  position:absolute;left:50px;top:467px;width:990px;height:1280px;
  background:var(--paper);overflow:hidden;
  transform:scale(1.1111);transform-origin:0 0;
}
.backdrop{position:absolute;inset:0}
.hero-photo{
  position:absolute;left:400px;top:40px;width:590px;height:520px;
  background:radial-gradient(ellipse at 45% 45%,var(--photo-a) 0%,var(--photo-b) 70%,#ffffff 100%);
}
.headline{
  position:absolute;left:42px;top:72px;
  font-family:"Bebas Neue",sans-serif;font-size:116px;line-height:88px;color:var(--ink);
}
.headline .accent{color:var(--blue)}
.headline-rule{position:absolute;left:45px;top:428px;width:80px;height:5px;background:var(--ink)}
.subhead{
  position:absolute;left:44px;top:460px;
  font-weight:700;font-size:23px;line-height:24px;color:var(--ink);letter-spacing:.3px;
}
.practice-seal{
  position:absolute;left:397px;top:432px;width:240px;height:240px;border-radius:50%;
  background:var(--paper);display:flex;align-items:center;justify-content:center;text-align:center;
  padding:30px;
}
.practice-seal span{font-weight:700;font-size:22px;line-height:28px;color:var(--navy);letter-spacing:.5px}
.section-title{
  position:absolute;font-family:"Bebas Neue",sans-serif;color:#fff;
}
.advantages-title{left:44px;top:700px;font-size:38px}
.advantages{position:absolute;left:0;top:745px;width:255px;list-style:none}
.advantages li{
  height:73px;margin-bottom:3px;padding:4px 0 0 44px;display:flex;align-items:center;
  background:linear-gradient(180deg,var(--blue-light),var(--blue));
  color:#fff;font-weight:700;font-size:21px;line-height:26px;letter-spacing:.6px;
}
.symptoms{position:absolute;top:694px;color:#fff}
.symptoms.women{left:290px}
.symptoms.men{left:602px}
.symptoms h2{font-weight:300;font-size:29px;line-height:30px;letter-spacing:.8px}
.symptoms h2 b{font-weight:700}
.symptoms .rule{width:36px;height:2px;background:#fff;margin:10px 0 16px}
.symptoms ul{list-style:none}
.symptoms li{position:relative;padding-left:25px;font-size:18.5px;line-height:24px;font-weight:400;white-space:nowrap}
.symptoms li::before{
  content:"";position:absolute;left:0;top:5px;width:15px;height:15px;border-radius:50%;background:var(--tick);
}
.symptoms li::after{
  content:"";position:absolute;left:4.5px;top:8px;width:5px;height:7px;
  border:solid #fff;border-width:0 2px 2px 0;transform:rotate(40deg);
}
.contact{position:absolute;left:44px;top:1122px;list-style:none;color:var(--ink)}
.contact li{display:flex;align-items:flex-start;gap:10px;font-size:17.5px;line-height:24.5px}
.contact li.strong{font-weight:600}
.contact svg{flex:none;margin-top:4px}
.doctor-band{position:absolute;left:0;top:0}
.doctor-photo{
  position:absolute;left:725px;top:1010px;width:260px;height:270px;
  background:linear-gradient(180deg,var(--doc-b) 0%,var(--doc-b) 38%,var(--doc-a) 40%,var(--doc-a) 100%);
  border-radius:120px 120px 0 0;
}
.doctor{position:absolute;left:450px;top:1112px;color:#fff}
.doctor h3{font-family:"Bebas Neue",sans-serif;font-weight:400;font-size:40px;line-height:38px}
.doctor .role{font-weight:300;font-size:25px;line-height:28px}
.doctor .rule{width:36px;height:2px;background:#fff;margin:14px 0 16px}
.doctor .tagline{font-weight:600;font-size:20px;line-height:26px}
</style>
</head>
<body>
<main class="flyer">
  <svg class="backdrop" width="990" height="1280" viewBox="0 0 990 1280" aria-hidden="true">
    <rect x="0" y="430" width="990" height="672" fill="var(--navy)"/>
  </svg>
  <div class="hero-photo" role="img" aria-label="Photo of a smiling mature couple embracing"></div>
  <svg class="backdrop" width="990" height="1280" viewBox="0 0 990 1280" aria-hidden="true">
    <path d="M0,0 H400 V560 H990 V445 C840,460 700,530 560,590 C420,650 200,640 0,510 Z" fill="var(--paper)"/>
    <path d="M0,0 H400 V430 H0 Z" fill="var(--paper)"/>
    <path d="M0,518 C200,640 420,650 560,592 L548,628 C400,690 200,680 0,580 Z" fill="var(--blue)"/>
    <path d="M560,592 C700,530 840,462 990,448 L990,470 C850,480 710,540 575,604 Z" fill="#ffffff" opacity=".9"/>
    <path d="M380,1280 L430,1087 H990 V1280 Z" fill="var(--blue)"/>
  </svg>

  <h1 class="headline"><span class="accent">Natural<br>Hormone</span><br>For Women<br>and Men</h1>
  <div class="headline-rule"></div>
  <p class="subhead">BY A PELLET<br>INSERTION PROCEDURE</p>

  <div class="practice-seal"><span>BROOKHAVEN<br>INTERNAL<br>MEDICINE</span></div>

  <h2 class="section-title advantages-title">Our Advantages</h2>
  <ul class="advantages">
    <li>QUALIFIED<br>PROVIDER</li>
    <li>MODERN<br>CONVENIENCE</li>
    <li>PERSONALIZED<br>CARE</li>
    <li>INDIVIDUAL<br>APPROACH</li>
  </ul>

  <section class="symptoms women">
    <h2>SYMPTOMS<br>FOR <b>WOMEN:</b></h2>
    <div class="rule"></div>
    <ul>
      <li>Fatigue*</li><li>Trouble sleeping*</li><li>Irritability*</li><li>Anxiousness*</li>
      <li>Mood swings*</li><li>Low mood*</li><li>Night sweats*</li><li>Hot flashes or flushes*</li>
      <li>Weight gain*</li><li>Decreased sex drive*</li><li>Discomfort during intercourse*</li><li>Low bone density*</li>
    </ul>
  </section>

  <section class="symptoms men">
    <h2>SYMPTOMS<br>FOR <b>MEN:</b></h2>
    <div class="rule"></div>
    <ul>
      <li>Low sex drive*</li><li>Increased body fat</li><li>(especially in the waist area)*</li>
      <li>Loss of muscle mass and strength*</li><li>Reduced mental focus*</li><li>Feelings of anxiety*</li>
      <li>Irritability*</li><li>Fatigue*</li><li>Elevated blood sugar*</li><li>High cholesterol*</li>
    </ul>
  </section>

  <ul class="contact">
    <li><svg width="16" height="16" viewBox="0 0 16 16"><path d="M8 1a5 5 0 0 0-5 5c0 4 5 9 5 9s5-5 5-9a5 5 0 0 0-5-5z" fill="none" stroke="var(--ink)" stroke-width="1.6"/><circle cx="8" cy="6" r="1.8" fill="var(--ink)"/></svg><span>4382 Larkspur Lane,<br>Columbia, SC. 20917</span></li>
    <li class="strong"><svg width="16" height="16" viewBox="0 0 16 16"><circle cx="8" cy="8" r="7" fill="none" stroke="var(--ink)" stroke-width="1.4"/><path d="M5.5 4.5l1.5 1.5-1 1a6 6 0 0 0 3 3l1-1 1.5 1.5-1 1c-2.5 0-5.5-3-5.5-5.5z" fill="var(--ink)"/></svg><span>803-671-5394</span></li>
    <li><svg width="16" height="16" viewBox="0 0 16 16"><circle cx="8" cy="8" r="7" fill="none" stroke="var(--ink)" stroke-width="1.4"/><rect x="4" y="5.5" width="8" height="5.5" fill="none" stroke="var(--ink)" stroke-width="1.2"/><path d="M4 5.5l4 3 4-3" fill="none" stroke="var(--ink)" stroke-width="1.2"/></svg><span>jtrevor@brookhavenimd.example</span></li>
    <li><svg width="16" height="16" viewBox="0 0 16 16"><circle cx="8" cy="8" r="7" fill="none" stroke="var(--ink)" stroke-width="1.4"/><ellipse cx="8" cy="8" rx="3" ry="7" fill="none" stroke="var(--ink)" stroke-width="1"/><path d="M1 8h14" stroke="var(--ink)" stroke-width="1"/></svg><span>www.brookhavenimd.example</span></li>
    <li><svg width="16" height="16" viewBox="0 0 16 16"><circle cx="8" cy="8" r="8" fill="var(--blue)"/></svg><span>/profile.php?id=70938265147723</span></li>
  </ul>

  <div class="doctor-photo" role="img" aria-label="Portrait of the physician in a maroon polo shirt"></div>
  <div class="doctor">
    <h3>Marcus D. Hollend II, DO</h3>
    <p class="role">Internal Medicine</p>
    <div class="rule"></div>
    <p class="tagline">My Philosophy and<br>Approach to Wellness...</p>
  </div>
</main>
</body>
</html>
```